Broschüre für eine Trainingsakademie
Zielgruppe
Ich möchte eine Broschüre zu meinem Unternehmen und meinen Angeboten schöner Design haben.
Ich bin Trainer/ Coach für moderne Personalstrategien insbesondere für die Personalgewinnung, Mitarbeiterbindung und -entwicklung. Zudem biete ich Trainings und Coachings für Mitarbeiter und Führungskräfte an. Zum Beispiel zu Themen wie gesunde Führung, Stressmanagement, Resilienz usw.
Meine Zielgruppe sind vor allem mittelständische Unternehmen oder junge aufstrebende StartUps, die ich beim Aufbau von Personalstrukturen unterstütze.
Aufgabenstellung
Mein Logo und die Farben sollen entsprechend berücksichtigt werden. Ein Entwurf für die Broschüre besteht bereits. Das ist allerdings nur meine Idee, als Laie. Ich hätte hier gern professionelle Ideen, so dass die Broschüre professionell und ansprechend wirkt.
Bilder habe ich eigentlich - diese finden sich auch auf meiner Homepage. Allerdings bin ich gerade auch beim Deckblatt offen. Auch für andere Gestaltungsvorschläge.

```html
<!DOCTYPE html>
<html lang="de">
<head>
<meta charset="utf-8">
<title>Broschüre – Trainingsangebot</title>
<link href="https://fonts.googleapis.com/css2?family=Arimo:wght@400;700&display=swap" rel="stylesheet">
<style>
  :root {
    --bg: #ecebf0;
    --page: #ffffff;
    --ink: #1f1f24;
    --ink-soft: #6b6a78;
    --brand: #5b4e85;
    --brand-light: #cfcbdc;
    --rule: #6f6796;
    --folio: #a9a7b8;
  }
  * { box-sizing: border-box; margin: 0; padding: 0; }
  html, body { width: 1200px; height: 600px; overflow: hidden; }
  body {
    background: var(--bg);
    font-family: "Arimo", Arial, sans-serif;
    color: var(--ink);
    position: relative;
  }
  .page {
    position: absolute;
    width: 549px;
    height: 387px;
    background: var(--page);
    overflow: hidden;
  }
  .page--eight { left: 27px; top: 28px; }
  .page--nine { left: 622px; top: 184px; }

  .page-deco { position: absolute; left: 0; top: 0; width: 549px; height: 387px; }

  .page-title {
    position: absolute;
    left: 41px; top: 36px;
    font-size: 16px;
    font-weight: 400;
    letter-spacing: 0.3px;
    white-space: nowrap;
  }
  .page-title strong { font-weight: 700; }

  .brand-name {
    position: absolute;
    left: 395px; top: 40px;
    width: 112px;
    text-align: center;
    color: var(--brand);
    font-size: 13px;
    font-weight: 700;
    letter-spacing: 0.6px;
    line-height: 16px;
  }
  .brand-name::after {
    content: "";
    display: block;
    height: 1px;
    background: var(--brand);
    margin-top: 1px;
  }

  .topic-list {
    position: absolute;
    list-style: none;
    font-size: 9.4px;
    line-height: 12.9px;
    text-align: justify;
  }
  .topic-list li { position: relative; padding-left: 8px; }
  .topic-list li::before {
    content: "•";
    position: absolute; left: 0; top: 0;
  }
  .topic-list--main { left: 41px; top: 66px; width: 216px; }
  .topic-list--side { left: 300px; top: 92px; width: 210px; }
  .page--nine .topic-list--main { width: 221px; }
  .page--nine .topic-list--side { top: 92px; width: 216px; }
  .fade { color: var(--ink-soft); }

  .artwork {
    position: absolute;
    left: 396px; top: 207px;
    width: 115px; height: 81px;
    background: var(--brand);
  }

  .section-label {
    position: absolute;
    left: 41px; top: 298px;
    font-size: 15.5px;
    font-weight: 400;
  }
  .section-label strong { font-weight: 700; }

  .folio {
    position: absolute;
    left: 488px; top: 354px;
    width: 20px; height: 33px;
    background: var(--folio);
    color: #fff;
    font-size: 14px;
    text-align: center;
    padding-top: 6px;
  }
</style>
</head>
<body>

<section class="page page--eight">
  <svg class="page-deco" viewBox="0 0 549 387" aria-hidden="true">
    <defs>
      <linearGradient id="fadeA" x1="0" y1="0" x2="1" y2="1">
        <stop offset="0" stop-color="#c9c5d8"/>
        <stop offset="1" stop-color="#ffffff" stop-opacity="0"/>
      </linearGradient>
      <linearGradient id="footA" x1="0" y1="0" x2="1" y2="0">
        <stop offset="0" stop-color="#dedbe6"/>
        <stop offset="0.6" stop-color="#ffffff" stop-opacity="0"/>
      </linearGradient>
    </defs>
    <polygon points="0,0 60,0 110,55 0,165" fill="url(#fadeA)" opacity="0.8"/>
    <polygon points="20,0 30,0 85,55 78,60" fill="#ffffff"/>
    <polygon points="40,0 90,0 112,22 80,40" fill="#d6d3e2" opacity="0.8"/>
    <polygon points="0,35 24,100 0,165" fill="#ffffff" opacity="0.7"/>
    <polygon points="0,293 549,293 549,330 0,360" fill="url(#footA)"/>
    <polyline points="257,45 298,45 298,219 392,219" fill="none" stroke="#444" stroke-width="0.8" stroke-dasharray="1 2"/>
    <line x1="0" y1="293" x2="549" y2="293" stroke="var(--rule)" stroke-width="1"/>
    <line x1="27" y1="276" x2="27" y2="355" stroke="var(--rule)" stroke-width="1"/>
  </svg>

  <h2 class="page-title">PERSONAL<strong>ENTWICKLUNG</strong></h2>
  <div class="brand-name">HALVORSEN<br><span style="font-size:6px;letter-spacing:1.5px;display:block;line-height:7px">COACHING</span></div>

  <ul class="topic-list topic-list--main">
    <li><span class="fade">Mitarbeiter</span> Coaching - Mental fit im <span class="fade">Arbeitsleben:</span> Stressmanagement, <span class="fade">Konfliktmanagement,</span> Motivationsthemen, <span class="fade">Mentale Stärke,</span> Resilienz und <span class="fade">Ressourcen</span>aufbau sind nur einige Inhalte, <span class="fade">die in</span> diesem Coachingprogramm neben <span class="fade">individ</span>uellen Themen bearbeitet werden.</li>
    <li>Mitarbeiter-Trainings/ Gruppentrainings: Ich biete Seminare zu Resilienz und Stressmanagement, effizientes und effektives Management/ Zeitmanagement, Ressourcenaufbau und mentale Stärke, Stressmanagement oder Konfliktmanagement an.</li>
  </ul>

  <ul class="topic-list topic-list--side">
    <li>Mitarbeiterbegleitung - Outplacement Unterstützen Sie Ihre Mitarbeiter im Trennungsprozess: Ich unterstütze Ihre Mitarbeiter bei der Bestandsaufnahme, Kompetenzanalyse, Karriereplanung sowie dem Bewerbungscoaching und begleite die Umsetzung bis hin zum neuen Job.</li>
  </ul>

  <div class="artwork" role="img" aria-label="Illustration: eine Gruppe laufender Geschäftsleute folgt einer Person mit Fahne"></div>

  <p class="section-label">Trainings<strong>angebot</strong></p>
  <div class="folio">8</div>
</section>

<section class="page page--nine">
  <svg class="page-deco" viewBox="0 0 549 387" aria-hidden="true">
    <defs>
      <linearGradient id="fadeB" x1="0" y1="0" x2="1" y2="1">
        <stop offset="0" stop-color="#c9c5d8"/>
        <stop offset="1" stop-color="#ffffff" stop-opacity="0"/>
      </linearGradient>
      <linearGradient id="footB" x1="0" y1="0" x2="1" y2="0">
        <stop offset="0" stop-color="#dedbe6"/>
        <stop offset="0.6" stop-color="#ffffff" stop-opacity="0"/>
      </linearGradient>
    </defs>
    <polygon points="0,0 60,0 110,55 0,165" fill="url(#fadeB)" opacity="0.8"/>
    <polygon points="20,0 30,0 85,55 78,60" fill="#ffffff"/>
    <polygon points="40,0 90,0 112,22 80,40" fill="#d6d3e2" opacity="0.8"/>
    <polygon points="0,35 24,100 0,165" fill="#ffffff" opacity="0.7"/>
    <polygon points="0,293 549,293 549,330 0,360" fill="url(#footB)"/>
    <polyline points="211,45 283,45 283,218 392,218" fill="none" stroke="#444" stroke-width="0.8" stroke-dasharray="1 2"/>
    <line x1="0" y1="293" x2="549" y2="293" stroke="var(--rule)" stroke-width="1"/>
    <line x1="27" y1="276" x2="27" y2="355" stroke="var(--rule)" stroke-width="1"/>
  </svg>

  <h2 class="page-title">PERSONAL<strong>FÜHRUNG</strong></h2>
  <div class="brand-name">HALVORSEN<br><span style="font-size:6px;letter-spacing:1.5px;display:block;line-height:7px">COACHING</span></div>

  <ul class="topic-list topic-list--main">
    <li>Führungskräfte Coaching - Mental fit Führen: (Digitale-) Führung, <span class="fade">Stressmanag</span>ement, Konfliktmanagement, <span class="fade">Motiv</span>ationsthemen, Mentale Stärke, Resilienz, <span class="fade">Ressourcen</span>aufbau und Zeitmanagement sind <span class="fade">nur einige</span> Inhalte, die in diesem <span class="fade">Coaching</span>programm neben individuellen Themen bearbeitet werden.</li>
    <li>Mitarbeiter Coaching - Auf dem Weg zur Führungskraft: Vorbereitung und Begleitung Ihres Mitarbeiters auf dem Weg zur Führungskraft.</li>
  </ul>

  <ul class="topic-list topic-list--side">
    <li>Gruppentrainings zu gesunder Führung: Mitarbeiter motivierend Führen, Vorbild sein, Stressmanagement , Konflikte meistern und effektive Führung sind hier einige Themen, die in diesem Training betrachtet werden.</li>
  </ul>

  <div class="artwork" role="img" aria-label="Illustration: eine Person springt von einem Sprungbrett über ein steigendes Balkendiagramm"></div>

  <p class="section-label">Trainings<strong>angebot</strong></p>
  <div class="folio">9</div>
</section>

</body>
</html>
```